New start-up company catalog!

Heat transfer printing company. We are set to launch later this month and need a stand out catalog to wow our customers. We are a printing/manufacturing heat transfer company geared towards apparel and promotional items.

```html
<!DOCTYPE html>
<html lang="en">
<head>
<meta charset="utf-8">
<title>Northway Prints – Catalog Cover Spread</title>
<link rel="stylesheet" href="https://fonts.googleapis.com/css2?family=Poppins:wght@700&family=Oswald:wght@700&family=Anton&display=swap">
<style>
  :root {
    --backdrop: #e4e4e6;
    --paper: #f6f6f7;
    --paper-shade: #e2e2e6;
    --brand-purple: #4b3f9b;
    --navy-band: #2f2a72;
    --lavender: #b9b4e3;
    --orange: #e99a22;
    --teal: #5ec7c2;
    --teal-light: #a6dfdc;
    --ink: #1d1b3a;
    --shirt-light: #e9e9ec;
    --shirt-dark: #222226;
    --bag-blue: #2f6fc4;
  }
  * { margin: 0; padding: 0; box-sizing: border-box; }
  html, body { width: 1200px; height: 900px; overflow: hidden; background: var(--backdrop); }

  .spread {
    position: absolute; left: 50px; top: 150px;
    width: 1100px; height: 600px;
    display: flex;
    box-shadow: 0 18px 40px rgba(0,0,0,.18);
  }
  .page { position: relative; width: 550px; height: 600px; overflow: hidden;
          background: linear-gradient(135deg, var(--paper) 40%, var(--paper-shade)); }
  .page-shapes { position: absolute; inset: 0; }

  .brand { position: absolute; display: flex; align-items: center; gap: 12px; }
  .brand-square { width: 44px; height: 44px; background: var(--brand-purple); }
  .brand-name { font-family: "Poppins", sans-serif; font-weight: 700; font-size: 34px;
                color: var(--brand-purple); letter-spacing: -0.5px; }

  .back-cover .brand { left: 70px; top: 80px; }
  .web-address { position: absolute; left: 120px; top: 331px; width: 210px;
                 font-family: "Oswald", sans-serif; font-weight: 700; font-size: 18px;
                 color: var(--ink); text-align: center; line-height: 26px; }
  .phone-number { position: absolute; left: 30px; top: 365px;
                  font-family: "Oswald", sans-serif; font-weight: 700; font-style: italic;
                  font-size: 46px; letter-spacing: 1px; color: var(--orange); line-height: 56px; }

  .front-cover .brand { left: 95px; top: 120px; }
  .front-cover .brand-square { width: 52px; height: 52px; }
  .front-cover .brand-name { font-size: 40px; }
  .headline { position: absolute; right: 70px; top: 195px; text-align: right;
              font-family: "Anton", sans-serif; text-transform: uppercase;
              transform: skewX(-12deg); line-height: 1; }
  .headline-top { display: block; font-size: 52px; color: var(--orange); }
  .headline-bottom { display: block; font-size: 46px; color: var(--teal); }

  .product { position: absolute; }
  .product-white-tee { left: 40px; top: 345px; width: 190px; height: 230px; border-radius: 14px;
                       background: linear-gradient(160deg, #fbfbfc, var(--shirt-light)); }
  .product-black-tee { left: 205px; top: 355px; width: 200px; height: 245px; border-radius: 14px;
                       background: linear-gradient(160deg, #34343a, var(--shirt-dark)); }
  .product-bag { left: 410px; top: 440px; width: 110px; height: 130px; border-radius: 10px;
                 background: linear-gradient(180deg, #1c2a48 55%, var(--bag-blue)); }
</style>
</head>
<body>
  <main class="spread">
    <section class="page back-cover">
      <svg class="page-shapes" viewBox="0 0 550 600" aria-hidden="true">
        <polygon points="430,0 550,0 550,600 260,600" fill="var(--navy-band)"/>
        <polygon points="0,330 340,330 332,356 0,356" fill="var(--orange)"/>
        <polygon points="0,356 318,356 296,440 0,440" fill="var(--brand-purple)"/>
        <line x1="350" y1="290" x2="296" y2="470" stroke="var(--teal)" stroke-width="6"/>
      </svg>
      <div class="brand">
        <span class="brand-square"></span>
        <span class="brand-name">Northway Prints</span>
      </div>
      <p class="web-address">www.yourweb.com</p>
      <p class="phone-number">0123 456 789</p>
    </section>

    <section class="page front-cover">
      <svg class="page-shapes" viewBox="0 0 550 600" aria-hidden="true">
        <defs>
          <linearGradient id="tealFade" x1="0" y1="0" x2="1" y2="0">
            <stop offset="0" stop-color="var(--teal-light)"/>
            <stop offset="1" stop-color="var(--teal)"/>
          </linearGradient>
        </defs>
        <polygon points="0,0 90,0 0,300" fill="var(--lavender)"/>
        <polygon points="475,0 550,0 550,600 400,600" fill="url(#tealFade)"/>
        <line x1="70" y1="210" x2="35" y2="320" stroke="var(--orange)" stroke-width="6"/>
        <line x1="395" y1="600" x2="550" y2="420" stroke="var(--brand-purple)" stroke-width="6"/>
      </svg>
      <div class="brand">
        <span class="brand-square"></span>
        <span class="brand-name">Northway Prints</span>
      </div>
      <h1 class="headline">
        <span class="headline-top">Quality</span>
        <span class="headline-bottom">Heat Transfers</span>
      </h1>
      <div class="product product-white-tee" role="img" aria-label="White T-shirt with a printed line-art graphic"></div>
      <div class="product product-black-tee" role="img" aria-label="Black T-shirt with a yellow and white lettering print"></div>
      <div class="product product-bag" role="img" aria-label="Navy and blue drawstring bag with a printed emblem"></div>
    </section>
  </main>
</body>
</html>
```